Flyer Design Project

We are offering a new class on cyber crime and want to advertise this course to students. We would like to see a design that is eye catching and coveys the goals of the course, when it meets and a brief abstract for the class.

The course will focus on the economics of cyber crime so including one or two graphics that get across this point would be good.

Requirements
Must have
• Course name "Cyber Crime"
Call number "CS 795 - 004"
Course meeting time (day of week and time) Tue. 4:30-7:10pm
Course goals
Course abstract

```html
<!DOCTYPE html>
<html lang="en">
<head>
<meta charset="utf-8">
<title>Cyber Crime – A New Course</title>
<link href="https://fonts.googleapis.com/css2?family=Alfa+Slab+One&family=Fira+Sans:ital,wght@0,400;0,700;1,400;1,800&family=Fira+Sans+Extra+Condensed:wght@600&family=Kaushan+Script&display=swap" rel="stylesheet">
<style>
  :root{
    --page:#ffffff;
    --frame:#0e1f4d;
    --navy:#0a2663;
    --royal:#0f4fa3;
    --sun:#fff04a;
    --skin:#efc7ad;
    --sign:#e89a78;
    --card-light:#dbe9f8;
    --card-deep:#2f79c6;
    --money:#cfd6c6;
    --ink:#111111;
    --red:#d3202a;
    --white:#ffffff;
  }
  *{margin:0;padding:0;box-sizing:border-box}
  html,body{width:1200px;height:900px;overflow:hidden;background:var(--page)}
  .flyer{position:absolute;left:284px;top:17px;width:660px;height:865px;border:2px solid var(--frame);background:var(--white)}
  .flyer-field{position:absolute;left:8px;top:8px;width:640px;height:845px;overflow:hidden;
    background:linear-gradient(160deg,var(--navy) 0%,var(--royal) 55%,var(--navy) 100%)}
  .backdrop{position:absolute;left:0;top:0}
  .mascot-art{position:absolute;left:16px;top:-10px;width:330px;height:445px;border-radius:165px 165px 4px 4px;
    background:linear-gradient(180deg,var(--skin) 0%,var(--skin) 50%,var(--sign) 75%,var(--sign) 100%)}
  .card-art{position:absolute;left:380px;top:40px;width:240px;height:160px;border-radius:14px;transform:rotate(-62deg);transform-origin:center;
    left:340px;top:90px;width:300px;height:185px;
    background:linear-gradient(135deg,var(--card-light) 0%,var(--card-deep) 100%);box-shadow:8px 10px 0 rgba(0,0,0,.35)}
  .title{position:absolute;left:22px;top:280px;width:600px;font-family:"Alfa Slab One",serif;font-size:122px;line-height:104px;
    color:var(--money);-webkit-text-stroke:3px var(--ink);letter-spacing:4px;text-shadow:6px 6px 0 rgba(0,0,0,.45)}
  .title span{display:block}
  .title .line-two{padding-left:18px}
  .tagline{position:absolute;left:22px;top:478px;font-family:"Kaushan Script",cursive;font-size:44px;color:var(--red);
    -webkit-text-stroke:1px var(--white);transform:rotate(-4deg);transform-origin:left bottom;text-shadow:2px 2px 0 var(--white)}
  .details{position:absolute;left:22px;top:527px;width:600px;color:var(--white);font-family:"Fira Sans",sans-serif}
  .call-number{font-style:italic;font-size:13px}
  .schedule{font-family:"Fira Sans Extra Condensed",sans-serif;font-weight:600;font-size:37px;line-height:44px;margin-top:4px}
  .section-head{font-weight:700;font-size:13px;text-decoration:underline;margin-top:8px;line-height:15px}
  .goals{list-style:none;font-size:13px;line-height:15px}
  .goals li{padding-left:14px;text-indent:-14px}
  .goals li+li{margin-top:16px}
  .abstract{font-size:13px;line-height:16px;width:595px}
  .url{position:absolute;left:22px;top:805px;font-family:"Fira Sans",sans-serif;font-weight:800;font-style:italic;font-size:30px;
    color:var(--red);text-shadow:3px 3px 2px rgba(0,0,0,.5);-webkit-text-stroke:1px var(--white)}
</style>
</head>
<body>
  <div class="flyer">
    <div class="flyer-field">
      <svg class="backdrop" width="640" height="460" aria-hidden="true">
        <ellipse cx="330" cy="270" rx="370" ry="190" fill="var(--sun)"/>
      </svg>
      <div class="mascot-art" role="img" aria-label="Cartoon bandit in a black eye mask holding up a sign reading SPAM"></div>
      <div class="card-art" role="img" aria-label="Tilted platinum credit card illustration"></div>
      <h1 class="title"><span>CYBER</span><span class="line-two">CRIME</span></h1>
      <p class="tagline">a new course</p>
      <div class="details">
        <p class="call-number">CS 795 / ISA 797</p>
        <p class="schedule">FALL 2012&nbsp;|&nbsp;TUESDAY&nbsp;|&nbsp;4:30 PM – 7:10 PM</p>
        <h2 class="section-head">COURSE GOALS</h2>
        <ol class="goals">
          <li>1) Understand how modern cyber-crime operates on a technical and economic level</li>
          <li>2) Analyze some of the potential places to intervene at an economic, technical and<br>policy level</li>
        </ol>
        <h2 class="section-head">COURSE ABSTRACT</h2>
        <p class="abstract">Arguably the single most significant change in the cyber-security landscape has been the explosive rise of profit-fueled cyber-crime. Obtaining a detailed, structural understanding of how profit-driven cyber crime works — its underlying economics and associated business practices — has the potential to illuminate new defensive measures that might prove far more efficient for countering attacks than purely technical measures. This research seminar will delve into our current understanding of the economics of cyber-crime.</p>
      </div>
      <p class="url">http://cs.northfield.edu/~vance/crime.html</p>
    </div>
  </div>
</body>
</html>
```